Veterinary Pylon

My veterinary clinic is not clearly visible from the street and I want to place a Pylon next to my driveway. I want a modern, elegant straight Design, the Photo shows the sheduled place. One can see the clinic on our Homepage: www.lindbrook-pet-klinik.at
The last pictures are examples for pylones I like

Target Market(s)

the passing cars often miss my entry...I want to show where to turn left

Colors
3276b5
33a6d7
00a990

Requirements
Must have
• High value, simple elegance, size: 250cm (high) x 100cm (width)
Nice to have
• Our Logo, arrow(?)

A special Text is not necessary but this will be an option:

Biegen sie hier ab und wir biegen es wieder hin!
Should not have
• Too much Color, the colors I have chosen are the possible colors but it‘s not necessary to use them.

```html
<!DOCTYPE html>
<html lang="de">
<head>
<meta charset="utf-8">
<title>Lindbrook Pet Klinik – Pylon</title>
<link rel="stylesheet" href="https://fonts.googleapis.com/css2?family=Montserrat:wght@600;700&display=swap">
<style>
  :root {
    --brand-blue: #2a4a8c;
    --sky-light: #eef5fc;
    --sky-mid: #cfe3f5;
    --steel-blue: #5b9ad6;
    --deep-blue: #1f5aa8;
    --white: #ffffff;
    --stage: #e9ecef;
  }
  * { margin: 0; padding: 0; box-sizing: border-box; }
  html, body {
    width: 818px;
    height: 1200px;
    overflow: hidden;
    background: var(--stage);
  }
  .pylon {
    position: absolute;
    left: 180px;
    top: 20px;
    width: 458px;
    height: 1160px;
    overflow: hidden;
    background: var(--sky-light);
    font-family: "Montserrat", sans-serif;
  }
  .pylon__photo {
    position: absolute;
    inset: 0;
    background:
      radial-gradient(ellipse 70% 22% at 62% 78%, var(--steel-blue) 0%, rgba(91,154,214,0.55) 40%, rgba(207,227,245,0) 75%),
      linear-gradient(180deg, var(--white) 0%, var(--sky-light) 45%, var(--sky-mid) 70%, #9cc4ea 100%);
  }
  .pylon__header {
    position: absolute;
    inset: 0;
    background: var(--brand-blue);
    clip-path: polygon(0 0, 100% 0, 100% 603px, 0 492px);
  }
  .brand {
    position: absolute;
    left: 0;
    right: 0;
    top: 70px;
    text-align: center;
    color: var(--white);
    font-weight: 700;
  }
  .brand__dot {
    display: block;
    width: 130px;
    height: 130px;
    margin: 0 auto 70px;
    border-radius: 50%;
    border: 6px solid var(--white);
  }
  .brand__name {
    font-size: 58px;
    line-height: 1;
    letter-spacing: 1px;
  }
  .brand__sub {
    display: flex;
    align-items: center;
    justify-content: center;
    gap: 14px;
    margin-top: 14px;
    font-size: 22px;
    letter-spacing: 8px;
  }
  .brand__rule {
    width: 70px;
    height: 3px;
    background: var(--white);
  }
  .slogan {
    position: absolute;
    left: 54px;
    top: 628px;
    color: var(--brand-blue);
    font-weight: 700;
    font-size: 38px;
    line-height: 49px;
  }
  .url-bar {
    position: absolute;
    left: 55px;
    right: 0;
    top: 1041px;
    height: 52px;
    background: var(--brand-blue);
    color: var(--white);
    font-weight: 600;
    font-size: 19px;
    display: flex;
    align-items: center;
    justify-content: center;
  }
</style>
</head>
<body>
  <div class="pylon">
    <div class="pylon__photo" role="img" aria-label="Foto: blaues Stethoskop auf spiegelnder, hellblauer Fläche"></div>
    <div class="pylon__header"></div>
    <div class="brand">
      <span class="brand__dot"></span>
      <div class="brand__name">LINDBROOK</div>
      <div class="brand__sub"><span class="brand__rule"></span>PET KLINIK<span class="brand__rule"></span></div>
    </div>
    <p class="slogan">Biegen Sie ein,<br>dann biegen wir<br>es hin!</p>
    <div class="url-bar">www.lindbrook-pet-klinik.at</div>
  </div>
</body>
</html>
```